Postcard design for Intellectual Property Professional Conference

Seeking design for 5.5" by 8.5" postcard mailer about a conference on tax and finance issues for international IP management. Attendees are lawyers and financial executives. Draft language is attached.

Target Market(s)

The project should have the attached picture of Boston with the caption "Courtesy of the Harborline Meetings & Travelers Council"

Industry/Entity Type

Finance

```html
<!DOCTYPE html>
<html lang="en">
<head>
<meta charset="utf-8">
<title>Intellectual Property in Developing Growth Markets – Postcard</title>
<link rel="stylesheet" href="https://fonts.googleapis.com/css2?family=Marcellus&family=Cabin:wght@400;500;600&family=Tinos&display=swap">
<style>
  :root{
    --page:#e9edf3;
    --navy:#1d3b66;
    --navy-deep:#13294b;
    --sky:#7fb2dc;
    --white:#ffffff;
    --ink:#1b1b1b;
    --rule:#3f5f8c;
  }
  *{box-sizing:border-box;margin:0;padding:0}
  html,body{width:1000px;height:1200px;overflow:hidden}
  body{background:linear-gradient(180deg,#f2f4f8 0%,var(--page) 100%);font-family:"Cabin",sans-serif;position:relative}

  .card{position:absolute;left:311px;width:611px;height:396px;background:var(--white);overflow:hidden;box-shadow:3px 5px 9px rgba(40,50,70,.35)}
  .card--front{top:115px}
  .card--back{top:665px}

  /* FRONT */
  .front-photo{position:absolute;left:0;top:0;width:611px;height:325px;
    background:linear-gradient(180deg,#8fb8df 0%,#a9c3db 25%,#7f9fbd 38%,#5d87ad 55%,#4a78a0 75%,#2f5a80 92%,#3c6b93 100%)}
  .front-topband{position:absolute;left:0;top:0;width:611px;height:10px;background:var(--sky)}
  .front-title{position:absolute;left:14px;top:16px;font-family:"Marcellus",serif;font-weight:400;color:var(--white);font-size:21.5px;line-height:31px;letter-spacing:.3px;text-transform:uppercase}
  .city{position:absolute;right:10px;top:14px;text-align:center;font-family:"Marcellus",serif;color:var(--navy)}
  .city__name{font-size:33px;letter-spacing:2px;line-height:38px}
  .city__date{font-size:15.5px;margin-top:1px}
  .early-badge{position:absolute;left:325px;top:52px;width:62px;height:62px;border-radius:50%;
    background:radial-gradient(circle at 40% 35%,#ffffff 0%,#dbe6f1 55%,#a9bfd6 100%);border:2px solid #c8d6e4;
    display:flex;flex-direction:column;align-items:center;justify-content:center;transform:rotate(-28deg);color:var(--navy);font-family:"Tinos",serif;line-height:1}
  .early-badge__small{font-size:8.5px}
  .early-badge__amount{font-size:17px;font-weight:700;margin-top:2px}
  .front-body{position:absolute;top:142px;color:var(--white);font-family:"Marcellus",serif;font-size:10.9px;line-height:14.6px;white-space:nowrap;text-shadow:0 0 1px rgba(20,40,70,.9),0 0 3px rgba(20,40,70,.5)}
  .front-body--left{left:15px}
  .front-body--right{left:322px}
  .photo-credit{position:absolute;left:3px;top:312px;font-family:"Tinos",serif;font-size:9px;color:var(--ink)}
  .front-footer{position:absolute;left:0;top:325px;width:611px;height:71px;background:linear-gradient(180deg,#f3f6fa,#ffffff)}
  .tagline{position:absolute;left:12px;top:14px;font-family:"Marcellus",serif;font-size:21px;color:var(--navy)}
  .tagline-rules{position:absolute;left:0;top:44px}

  /* organisation name */
  .org{position:absolute;display:flex;flex-direction:column;align-items:flex-start}
  .org__row{display:flex;align-items:center;gap:7px}
  .org__mark{width:16px;height:16px;background:var(--navy)}
  .org__name{font-family:"Cabin",sans-serif;font-weight:600;font-size:13px;color:var(--navy);line-height:1}
  .org__motto{font-size:7.5px;color:#2a2a2a;margin-top:5px;padding-left:23px}
  .card--front .org{left:395px;top:22px}

  /* BACK */
  .back-photo{position:absolute;left:0;top:0;width:611px;height:396px;
    background:linear-gradient(180deg,#7fb3e0 0%,#b9d2e7 22%,#c9b9a6 45%,#a17866 62%,#6f7d8a 75%,#8c6e5d 100%)}
  .topics-panel{position:absolute;left:0;top:0;width:298px;height:336px;background:linear-gradient(90deg,rgba(110,150,190,.6),rgba(150,180,210,.45))}
  .topics-heading{position:absolute;left:17px;top:9px;font-family:"Marcellus",serif;font-weight:400;color:var(--navy-deep);font-size:12px;letter-spacing:.3px}
  .topics{position:absolute;left:8px;top:22px;list-style:none;color:var(--white);font-family:"Marcellus",serif;font-size:10.9px;line-height:14.1px;white-space:nowrap;text-shadow:0 0 1px rgba(20,40,70,.9),0 0 3px rgba(20,40,70,.5)}
  .topics li{padding-left:10px;position:relative}
  .topics li::before{content:"";position:absolute;left:1px;top:5px;width:5px;height:5px;border-radius:50%;background:var(--white)}
  .back-credit{position:absolute;right:8px;top:3px;font-family:"Tinos",serif;font-size:9px;color:var(--ink)}
  .stamp-box{position:absolute;left:516px;top:19px;width:90px;height:107px;background:var(--white);border-radius:8px}
  .address-box{position:absolute;left:354px;top:229px;width:252px;height:162px;background:var(--white);border-radius:8px}
  .back-footer{position:absolute;left:0;top:336px;width:298px;height:60px;background:linear-gradient(180deg,#eef3f8,#ffffff)}
  .card--back .org{left:44px;top:13px}
</style>
</head>
<body>

<section class="card card--front" aria-label="Postcard front">
  <div class="front-photo" role="img" aria-label="Photo of the Boston harbor skyline with a boat on the water"></div>
  <div class="front-topband"></div>
  <h1 class="front-title">Intellectual Property<br>in Developing<br>Growth Markets</h1>
  <div class="early-badge">
    <span class="early-badge__small">Register Early</span>
    <span class="early-badge__small">and Save up to</span>
    <span class="early-badge__amount">$300</span>
  </div>
  <div class="city">
    <div class="city__name">BOSTON</div>
    <div class="city__date">March 24 &amp; 25, 2016</div>
  </div>
  <p class="front-body front-body--left">You are cordially invited to attend a comprehensive<br>and practical day and a half conference to examine<br>the tax and legal structuring strategies for<br>increasing profits from intellectual properties while<br>protecting these important assets when doing<br>business in fast growing developing markets.<br>Intellectual property assets include some of the<br>most important assets of most companies: their<br>patents, trade marks, copyrights, brand names and<br>licensing agreements.</p>
  <p class="front-body front-body--right">Senior tax, legal and financial experts will provide<br>a comprehensive analysis of the legal issues,<br>recent tax &amp; regulatory developments, skills and<br>structuring strategies necessary to maximize profits<br>from IP Migrating IP assets to low tax jurisdiction<br>will also be covered along with dealing with issues<br>of piracy, counterfeiting, infringement and other<br>legal challenges to a company's IP.</p>
  <p class="photo-credit">Boston Harbor Skyline - credit: Harborline Meetings &amp; Travelers Council</p>
  <div class="front-footer">
    <p class="tagline">Increasing Profits &amp; Protecting</p>
    <svg class="tagline-rules" width="380" height="14" viewBox="0 0 380 14" aria-hidden="true">
      <line x1="0" y1="2" x2="375" y2="2" stroke="var(--rule)" stroke-width="1"/>
      <line x1="0" y1="6" x2="360" y2="6" stroke="var(--rule)" stroke-width="1"/>
      <line x1="0" y1="10" x2="345" y2="10" stroke="var(--rule)" stroke-width="1"/>
    </svg>
    <div class="org">
      <div class="org__row"><span class="org__mark"></span><span class="org__name">Northbridge Markets Forum</span></div>
      <span class="org__motto">Cross-border briefings for corporate counsel</span>
    </div>
  </div>
</section>

<section class="card card--back" aria-label="Postcard back">
  <div class="back-photo" role="img" aria-label="Photo of Boston HarborWalk with lamp post and downtown towers"></div>
  <div class="topics-panel"></div>
  <h2 class="topics-heading">TOPICS TO BE COVERED INCLUDE:</h2>
  <ul class="topics">
    <li>Market trends in IP tax &amp; legal structures</li>
    <li>Proposed US Tax changes and regulatory<br>developments outside the US including European<br>and OECD developments affecting IP, patent box<br>base erosion and profit splitting (BEPS)</li>
    <li>Overview of the IP landscape in key developing<br>growth markets such as China, India, Brazil,<br>Korea, South Africa, Mexico and other developing<br>markets outside the US.</li>
    <li>Legal issues including litigation, arbitration and<br>use of government assistance to protect IP values<br>in key developing markets.</li>
    <li>Monetizing IP assets and rights in regard to<br>divestitures, spin offs, split offs, M&amp;A, transfers<br>of ownership and securitizations in developing<br>growth markets</li>
    <li>Special Tax Planning and Legal Considerations<br>for IP in Particular Sectors such as<br>Biopharmaceutical, International Sports Licensing,<br>High Tech, Consumer Brands, and Manufacturing</li>
    <li>Restructuring and Migration of IP Assets to<br>Tax Advantaged Jurisdictions.</li>
  </ul>
  <p class="back-credit">Boston HarborWalk-credit: Harbor Walkways Society</p>
  <div class="stamp-box"></div>
  <div class="address-box"></div>
  <div class="back-footer">
    <div class="org">
      <div class="org__row"><span class="org__mark"></span><span class="org__name">Northbridge Markets Forum</span></div>
      <span class="org__motto">Cross-border briefings for corporate counsel</span>
    </div>
  </div>
</section>

</body>
</html>
```